Honeyvale Stitchery Needs a Beautiful Website

I need a new website for this new E-commerce. I sell handmade baby crochets, e.g. booties, headbands, hats, etc. I need a feminine and soft design to make the moms-to-be say 'oohh ahh'. I'd like pink, blue and gray. I'd like an inviting homepage, and nice regular pages where people can see and order the products.

Industry/Entity Type

Baby

Requirements
Must have
• beautiful, soft, feminine design. Please use pictures of the colors I'd like: brown, yellow, pink and blue. Any combination, but definitely include brown.

```html
<!DOCTYPE html>
<html lang="en">
<head>
<meta charset="utf-8">
<title>Honeyvale Stitchery</title>
<link href="https://fonts.googleapis.com/css2?family=Quicksand:wght@500;600;700&family=Open+Sans:wght@400;600;700&display=swap" rel="stylesheet">
<style>
:root{
  --brown:#2b0f0a;
  --pink:#ec2c85;
  --pink-dark:#d81d74;
  --cyan:#1db8d9;
  --cyan-dark:#17a4c3;
  --text:#555;
  --muted:#999;
  --line:#e6e6e6;
  --foot:#f3f3f3;
}
*{margin:0;padding:0;box-sizing:border-box}
html,body{width:759px;height:1200px;overflow:hidden}
body{background:var(--brown);font-family:"Open Sans",sans-serif;color:var(--text);position:relative}
.abs{position:absolute}
.page{left:75px;top:0;width:610px;height:982px;background:#fff}
.top-rule{left:0;top:4px;width:759px;border-top:1px dashed #f07ab3}
.top-links{right:95px;top:12px;font-size:8px;color:var(--muted)}
.top-links span{margin:0 3px;color:#bbb}
.brand{left:90px;top:52px;display:flex;align-items:center;gap:6px;font-family:"Quicksand",sans-serif;font-weight:700;font-size:16px;line-height:20px;color:var(--pink);white-space:nowrap}
.brand i{width:10px;height:10px;border-radius:50%;background:var(--cyan);display:block;flex:none}
.search{left:295px;top:49px;width:242px;height:26px;border:2px solid #e2e2e2;border-radius:13px;font-size:8px;color:#999;padding:7px 12px}
.search svg{position:absolute;right:8px;top:5px}
.cart{left:600px;top:48px}
.cart-text{left:626px;top:52px;font-family:"Quicksand",sans-serif;font-size:10px;color:#444;line-height:12px}
.cart-text b{display:block;color:var(--pink);font-weight:600;font-size:12px}
.nav{left:75px;top:90px;width:610px;height:32px;background:var(--cyan);display:flex;font-family:"Quicksand",sans-serif;font-weight:700;font-size:11px;color:#fff}
.nav a{flex:auto;display:flex;align-items:center;justify-content:center;border-right:1px solid var(--cyan-dark);text-decoration:none;color:#fff}
.nav a:last-child{border-right:0}
.hero{left:77px;top:124px;width:604px;height:251px;border:2px solid #eee;background:#fff;overflow:hidden}
.hero-photo{left:320px;top:0;width:282px;height:247px;background:radial-gradient(circle at 45% 40%,#f7e4d8 0,#eee5e0 45%,#fff 80%)}
.hero h1{left:35px;top:64px;font-family:"Quicksand",sans-serif;font-weight:500;font-size:24px;color:var(--pink)}
.hero h2{left:35px;top:94px;font-family:"Quicksand",sans-serif;font-weight:500;font-size:14px;color:var(--cyan)}
.hero p{left:35px;top:118px;width:260px;font-size:7.5px;line-height:12px;color:#888}
.btn{background:var(--pink);color:#fff;font-weight:700;font-size:7.5px;text-transform:uppercase;border-radius:2px;display:flex;align-items:center;justify-content:center}
.hero .btn{left:35px;top:150px;width:82px;height:23px;font-size:8px}
.dots{left:270px;top:230px;width:66px;height:17px;background:#eee;border-radius:10px 10px 0 0;display:flex;gap:3px;justify-content:center;align-items:center}
.dots i{width:7px;height:7px;border-radius:50%;background:#bbb;display:block}
.dots i:first-child{background:var(--pink)}
.welcome{left:75px;top:405px;width:610px;text-align:center}
.welcome h2{font-family:"Quicksand",sans-serif;font-weight:500;font-size:19px;color:#444}
.welcome p{margin:6px auto 0;width:575px;font-size:7.8px;line-height:13px;color:#888}
.divider{left:75px;top:507px;width:610px;border-top:1px solid #eee}
.featured{left:94px;top:536px;font-family:"Quicksand",sans-serif;font-weight:500;font-size:15px;color:var(--cyan)}
.card{width:136px}
.card .ph{height:94px;border:1px solid #ddd}
.card h3{margin-top:6px;font-family:"Quicksand",sans-serif;font-weight:500;font-size:10.5px;color:#555}
.card p{margin-top:4px;font-size:7px;line-height:12px;color:#999}
.card .btn{margin-top:6px;width:65px;height:18px}
.footer{left:0;top:982px;width:759px;height:218px;background:var(--foot);border-top:1px dashed #ddd}
.col{top:26px}
.col h4{font-family:"Quicksand",sans-serif;font-weight:500;font-size:14px;color:#555;margin-bottom:8px}
.col li{list-style:none;font-size:8px;line-height:16px;color:#666}
.pay{display:flex;gap:4px;margin-top:6px}
.pay i{display:block;width:23px;height:13px;border:1px solid #ccc;background:#fff}
.foot-rule{left:0;top:175px;width:759px;border-top:1px solid #e4e4e4}
.copy{left:89px;top:191px;font-size:8px;color:#777}
.social{left:618px;top:189px;display:flex;gap:6px}
.social i{display:block;width:13px;height:13px;background:#3a6fa8;border-radius:2px}
.social i:nth-child(2){background:#4fc0e8}
.social i:nth-child(3){background:#1a6aa8}
</style>
</head>
<body>
<div class="abs top-rule"></div>
<div class="abs page"></div>

<header>
  <div class="abs top-links">View Cart<span>|</span>Register<span>|</span>Login<span>|</span>My Account</div>
  <div class="abs brand"><i></i>Honeyvale Stitchery</div>
  <div class="abs search">Type your word here
    <svg width="14" height="14" viewBox="0 0 14 14"><circle cx="6" cy="6" r="4.5" fill="none" stroke="#bbb" stroke-width="1.5"/><line x1="9.3" y1="9.3" x2="13" y2="13" stroke="#bbb" stroke-width="1.6"/></svg>
  </div>
  <svg class="abs cart" width="20" height="26" viewBox="0 0 20 26"><path d="M6 9V6a4 4 0 0 1 8 0v3" fill="none" stroke="#ccc" stroke-width="1.5"/><rect x="0" y="9" width="20" height="17" fill="#ccc"/></svg>
  <div class="abs cart-text">My Cart<b>0 items</b></div>
  <nav class="abs nav">
    <a>Home</a><a>About Us</a><a>Products</a><a>Specials</a><a>Order Now</a><a>Best Selling</a><a>Support</a><a>Contact</a>
  </nav>
</header>

<section class="abs hero">
  <div class="abs hero-photo" role="img" aria-label="Smiling baby wearing a blue crochet crown headband"></div>
  <h1 class="abs">We Sell Baby Crochets</h1>
  <h2 class="abs">Morbi ullamcorper nonummy</h2>
  <p class="abs">Donec scelerisque leo ac risus Praesent sit amet est In dictum dolor eu dictum porttitor enim felis viverra mi eget luctus</p>
  <div class="abs btn">View Product</div>
  <div class="abs dots"><i></i><i></i><i></i><i></i></div>
</section>

<section class="abs welcome">
  <h2>Welcome to Honeyvale Stitchery</h2>
  <p>Pellentesque faucibus Ut accumsan ultricies elit Maecenas at justo id velit placerat molestie Donec dictum lectus non odio Cras a ante vitae enim iaculis aliquam Mauris nunc quam venenatis nec euismod sit amet egestas placerat est Pellentesque habitant morbi tristique senectus et netus et malesuada fames ac turpis egestas Cras id elit Integer quis urna Ut ante enim dapibus malesuada fringilla eu condimentum quis tellus</p>
</section>
<div class="abs divider"></div>

<h2 class="abs featured">Featured Products</h2>

<div class="abs card" style="left:90px;top:568px"><div class="ph" role="img" aria-label="Black crochet baby sneakers" style="background:linear-gradient(#9a9a9a,#2a2a2a)"></div><h3>Product Name</h3><p>Donec dictum lectus non odio Cras ante vitae enim iaculis aliquam</p><div class="btn">Add to Cart</div></div>
<div class="abs card" style="left:238px;top:568px"><div class="ph" role="img" aria-label="Brown crochet baby sneakers with pink star" style="background:linear-gradient(#b79a8a,#4a3128)"></div><h3>Product Name</h3><p>Donec dictum lectus non odio Cras ante vitae enim iaculis aliquam</p><div class="btn">Add to Cart</div></div>
<div class="abs card" style="left:385px;top:568px"><div class="ph" role="img" aria-label="Pink crochet baby slippers with roses" style="background:linear-gradient(#efe8e4,#e8b9c4)"></div><h3>Product Name</h3><p>Donec dictum lectus non odio Cras ante vitae enim iaculis aliquam</p><div class="btn">Add to Cart</div></div>
<div class="abs card" style="left:533px;top:568px"><div class="ph" role="img" aria-label="Navy crochet baby high-top with red star" style="background:linear-gradient(#d9d9e0,#2c3b78)"></div><h3>Product Name</h3><p>Donec dictum lectus non odio Cras ante vitae enim iaculis aliquam</p><div class="btn">Add to Cart</div></div>

<div class="abs card" style="left:90px;top:767px"><div class="ph" role="img" aria-label="Grey crochet baby shoe with red flower" style="background:linear-gradient(#8a8a8a,#4e5a60)"></div><h3>Product Name</h3><p>Donec dictum lectus non odio Cras ante vitae enim iaculis aliquam</p><div class="btn">Add to Cart</div></div>
<div class="abs card" style="left:238px;top:767px"><div class="ph" role="img" aria-label="Navy crochet baby sneakers" style="background:linear-gradient(#8c8c8c,#2b3557)"></div><h3>Product Name</h3><p>Donec dictum lectus non odio Cras ante vitae enim iaculis aliquam</p><div class="btn">Add to Cart</div></div>
<div class="abs card" style="left:385px;top:767px"><div class="ph" role="img" aria-label="Pink crochet crown headband" style="background:linear-gradient(#f1e6ee,#ea6fc0)"></div><h3>Product Name</h3><p>Donec dictum lectus non odio Cras ante vitae enim iaculis aliquam</p><div class="btn">Add to Cart</div></div>
<div class="abs card" style="left:533px;top:767px"><div class="ph" role="img" aria-label="Cream crochet baby shoes with pink roses" style="background:linear-gradient(#c9c4bc,#ede6d4)"></div><h3>Product Name</h3><p>Donec dictum lectus non odio Cras ante vitae enim iaculis aliquam</p><div class="btn">Add to Cart</div></div>

<footer class="abs footer">
  <div class="abs col" style="left:89px"><h4>Products</h4><ul><li>Name Labels</li><li>Clothing Labels</li><li>Shoe Labels</li><li>Stick On Clothing Labels</li><li>Backpacks</li></ul></div>
  <div class="abs col" style="left:226px"><h4>Categories</h4><ul><li>Christmas</li><li>Halloween</li><li>Kids Bags</li><li>Stationery</li><li>Personalised Clothing</li></ul></div>
  <div class="abs col" style="left:368px"><h4>Best Selling</h4><ul><li>Personalised Wooden Puzzles</li><li>Wooden Name Puzzle</li><li>Personalised Teddy Bear</li><li>Story Books</li><li>Backpacks</li></ul></div>
  <div class="abs col" style="left:530px"><h4>Information</h4><ul><li>About Us</li><li>Order Now</li><li>Support</li><li>Shipping &amp; Return</li><li>Contact Us</li></ul>
    <div class="pay"><i></i><i></i><i></i><i></i></div>
  </div>
  <div class="abs foot-rule"></div>
  <div class="abs copy">© 2014 Company Name &nbsp;All right reserved &nbsp;Term of Use</div>
  <div class="abs social"><i></i><i></i><i></i></div>
</footer>
</body>
</html>
```